Harlow Crest Holdings (Remodeling company) needs a logo and business card

We need a business card design for a new company. We "flip" upmarket houses (buy, remodel and sell) in the Austin, TX area. I'd like neutral colors (grey, white, gold black). I would like it to include a simple, clean logo. Our designs are modern and uncluttered and I would like that reflected in the business card design.

Target Market(s)

Young professionals, Families, Retirees. Our properties will sell for $750k+

Industry/Entity Type

Real Estate

Contact Information for Business Card

Harlow Crets Holdings
Mona Harlow
(979) 555 0142
Owner
Rolf Tandem
(512) 555 0176
Realtor

Logo Text

Harlow Crest Holdings

Font styles to use
Serif
Script

Requirements
Must have
• Simple, classic design
Nice to have
• Clean lines, modern look
Should not have
• Too traditionally

```html
<!DOCTYPE html>
<html lang="en">
<head>
<meta charset="utf-8">
<title>Harlow Crets Holdings – Business Card</title>
<link rel="stylesheet" href="https://fonts.googleapis.com/css2?family=Alegreya:wght@400;500&family=Open+Sans:wght@400&display=swap">
<style>
  :root {
    --backdrop: #7a7a7a;
    --card-light: #ececec;
    --card-mid: #c9c9c9;
    --card-grey: #8e8e8e;
    --strip: #efefef;
    --ink-dark: #3a3a3a;
    --ink-light: #f7f7f7;
    --ink-soft: #555555;
  }
  html, body {
    margin: 0;
    padding: 0;
    width: 1200px;
    height: 1200px;
    overflow: hidden;
    background: var(--backdrop);
  }
  .canvas {
    width: 1200px;
    height: 1200px;
    display: flex;
    align-items: center;
    justify-content: center;
  }
  .card {
    position: relative;
    width: 1000px;
    height: 572px;
    background: var(--card-light);
    box-shadow: 0 12px 30px rgba(0,0,0,0.25);
    overflow: hidden;
  }
  .card-field {
    position: absolute;
    left: 0;
    top: 0;
    width: 1000px;
    height: 420px;
  }
  .brand {
    position: absolute;
    left: 70px;
    top: 66px;
    display: flex;
    align-items: center;
    gap: 16px;
  }
  .brand-square {
    width: 40px;
    height: 40px;
    background: var(--ink-dark);
    border-radius: 6px;
  }
  .brand-name {
    font-family: "Alegreya", serif;
    font-size: 22px;
    color: var(--ink-dark);
  }
  .company-title {
    position: absolute;
    left: 430px;
    top: 70px;
    font-family: "Alegreya", serif;
    font-size: 46px;
    color: var(--ink-light);
    letter-spacing: 0.5px;
  }
  .contact-strip {
    position: absolute;
    left: 0;
    bottom: 0;
    width: 1000px;
    height: 152px;
    background: var(--strip);
  }
  .primary-contact {
    position: absolute;
    left: 70px;
    top: 34px;
  }
  .primary-name {
    font-family: "Alegreya", serif;
    font-size: 44px;
    color: var(--ink-dark);
    line-height: 1;
    letter-spacing: 1px;
  }
  .primary-phone {
    font-family: "Open Sans", sans-serif;
    font-size: 22px;
    color: var(--ink-soft);
    margin-top: 8px;
  }
  .secondary-contact {
    position: absolute;
    right: 70px;
    top: 22px;
    text-align: right;
    font-family: "Open Sans", sans-serif;
    font-size: 18px;
    line-height: 1.45;
    color: var(--ink-soft);
  }
</style>
</head>
<body>
  <div class="canvas">
    <div class="card">
      <svg class="card-field" viewBox="0 0 1000 420" aria-hidden="true">
        <defs>
          <linearGradient id="fieldGrey" x1="0" y1="0" x2="1" y2="0">
            <stop offset="0" stop-color="#a9a9a9"/>
            <stop offset="1" stop-color="#8a8a8a"/>
          </linearGradient>
        </defs>
        <rect width="1000" height="420" fill="#e8e8e8"/>
        <path d="M360 0 H1000 V420 H300 C430 330 440 120 360 0 Z" fill="url(#fieldGrey)"/>
      </svg>

      <div class="brand">
        <div class="brand-square"></div>
        <div class="brand-name">Harlow Crets Holdings</div>
      </div>

      <div class="company-title">Harlow Crets Holdings</div>

      <div class="contact-strip">
        <div class="primary-contact">
          <div class="primary-name">Mona Harlow</div>
          <div class="primary-phone">(979) 555 0142</div>
        </div>
        <div class="secondary-contact">
          <div>Owner</div>
          <div>Rolf Tandem</div>
          <div>(512) 555 0176</div>
          <div>Realtor</div>
        </div>
      </div>
    </div>
  </div>
</body>
</html>
```